CNC Machine Shop Website
Corlinden Steel Forge
CNC Machine Shop Website - Manufacturing
Creative Brief
Manufacturing
www.CorlindenSteelForge.example
Blue
Brown
Silver/Grey
Arial, Verdana, Trebuchet MS, Times New Roman, Century Gothic, Georgia
http://www.pethwickmill.example/
http://www.volbra.example/home.html

```html
<!DOCTYPE html>
<html lang="en">
<head>
<meta charset="utf-8">
<title>Corlinden Steel Forge — CNC Machine Shop</title>
<link href="https://fonts.googleapis.com/css2?family=Arimo:wght@400;700&display=swap" rel="stylesheet">
<style>
:root{
  --navy-deep:#06203f;
  --navy:#0b3a6e;
  --blue:#1a5fa6;
  --blue-light:#3d8fd6;
  --sky:#9fc9ef;
  --bronze:#b8823c;
  --bronze-light:#d9a55c;
  --silver:#e4e6e9;
  --silver-mid:#c9cdd2;
  --grey-text:#6c7278;
  --white:#ffffff;
  --yellow:#f5c518;
}
*{margin:0;padding:0;box-sizing:border-box}
html,body{width:1200px;height:1014px;overflow:hidden}
body{font-family:"Arimo",Arial,sans-serif;background:var(--silver);position:relative;color:var(--white)}
.abs{position:absolute}

/* header */
.site-header{left:0;top:0;width:1200px;height:96px;background:linear-gradient(#ffffff,#e9ebee)}
.brand{left:160px;top:22px;display:flex;align-items:center;gap:14px}
.brand-mark{width:40px;height:40px;background:var(--blue)}
.brand-name{font-size:30px;font-weight:700;color:var(--navy);letter-spacing:1px;text-transform:uppercase}
.quote-btn{left:822px;top:26px;width:220px;height:48px;border-radius:6px;background:linear-gradient(#fdfdfd,#d7dbe0);border:1px solid var(--silver-mid);color:var(--navy);font-size:23px;font-weight:700;display:flex;align-items:center;justify-content:center;gap:10px}
.quote-btn::before{content:"";width:26px;height:26px;border-radius:4px;background:var(--bronze)}

/* blue stage */
.stage{left:0;top:96px;width:1200px;height:450px;background:linear-gradient(180deg,var(--navy-deep) 0%,var(--navy) 50%,#0d2f58 100%)}
.main-nav{left:150px;top:113px;width:900px;height:48px;border-radius:6px;background:linear-gradient(var(--blue-light),var(--navy));display:flex;font-size:15px;font-weight:700;text-transform:uppercase}
.main-nav a{color:var(--white);text-decoration:none;display:flex;align-items:center;justify-content:center;border-right:1px solid rgba(255,255,255,.25)}
.main-nav a:last-child{border-right:none}
.main-nav .active{background:linear-gradient(var(--bronze-light),var(--bronze))}
.dropdown{left:384px;top:161px;width:220px;background:var(--navy-deep);padding:6px 0;z-index:3;font-size:17px}
.dropdown li{list-style:none;padding:7px 20px}
.dropdown li.current{background:var(--blue)}

.hero-photo{left:150px;top:170px;width:576px;height:350px;background:linear-gradient(120deg,#8ab6d9 0%,#3f6f9a 45%,#1f3550 100%)}
.hero-caption{left:150px;top:466px;width:576px;height:54px;background:rgba(6,32,63,.85);display:flex;align-items:center;padding-left:14px;font-size:27px;font-weight:700;text-transform:uppercase}
.slider-dots{left:646px;top:480px;display:flex;gap:8px}
.slider-dots span{width:26px;height:26px;border-radius:50%;background:var(--blue);border:2px solid var(--white)}
.hero-panel{left:726px;top:170px;width:324px;height:290px;background:linear-gradient(var(--blue),var(--navy));padding:22px 18px}
.hero-panel h2{font-size:22px;line-height:1.15;text-transform:uppercase;color:var(--yellow)}
.hero-panel h2 span{display:block;color:var(--white)}
.hero-panel h3{font-size:15px;margin-top:6px;text-transform:uppercase}
.svc-list{display:grid;grid-template-columns:1fr 1fr;gap:6px 10px;margin-top:14px;font-size:14px}
.svc-list li{list-style:none}
.svc-list li::before{content:"› ";color:var(--sky);font-weight:700}
.panel-btn{margin-top:18px;width:210px;height:34px;border-radius:17px;background:rgba(255,255,255,.2);font-size:14px;display:flex;align-items:center;padding-left:40px}
.contact-strip{left:726px;top:460px;width:324px;height:64px;background:var(--white);color:var(--navy-deep);padding:8px 14px;font-size:14px;font-weight:700}
.contact-strip .phone{font-size:26px;color:var(--navy);line-height:1.05}
.contact-strip .mail{font-size:12px;font-weight:400}

/* features */
.feature{top:580px;width:290px;height:270px}
.feature-photo{width:290px;height:132px;background:linear-gradient(135deg,#5f7a94,#1c2c3e)}
.feature-title{height:40px;background:linear-gradient(var(--blue),var(--navy-deep));display:flex;align-items:center;padding-left:14px;font-size:17px;font-weight:700;text-transform:uppercase}
.feature-title em{font-style:normal;color:var(--bronze-light);margin-left:5px}
.feature-body{padding:12px 14px;font-size:13px;line-height:1.3;color:var(--grey-text);height:70px}
.read-more{margin:6px 14px 0 auto;width:80px;height:22px;border-radius:3px;background:var(--navy);font-size:12px;font-weight:700;display:flex;align-items:center;justify-content:center}

/* footer */
.site-footer{left:0;top:870px;width:1200px;height:102px;background:var(--navy-deep)}
.foot-col{top:888px;font-size:12px;line-height:1.5}
.foot-col h4{font-size:13px;margin-bottom:8px}
.foot-col a{color:var(--sky)}
.foot-bar{left:0;top:972px;width:1200px;height:42px;background:#04172e;font-size:12px;display:flex;align-items:center;justify-content:space-between;padding:0 150px;color:var(--sky)}
.foot-bar nav{display:flex;gap:22px}
.foot-bar nav a{color:var(--white);text-decoration:none}
.foot-bar nav a:first-child{color:var(--yellow)}
</style>
</head>
<body>
<header class="site-header abs">
  <div class="brand abs"><span class="brand-mark"></span><span class="brand-name">Corlinden Steel Forge</span></div>
  <div class="quote-btn abs">Request a Quote</div>
</header>

<section class="stage abs"></section>

<nav class="main-nav abs">
  <a style="width:90px">Home</a>
  <a style="width:100px">About Us</a>
  <a class="active" style="width:130px">Our Services</a>
  <a style="width:150px">Our Machines</a>
  <a style="width:150px">Quote Request</a>
  <a style="flex:1">Contact Us</a>
</nav>
<ul class="dropdown abs">
  <li>Machining</li><li>Powder Coating</li><li class="current">Forming</li><li>Welding</li><li>Plasma Cutting</li><li>Prototyping</li>
</ul>

<div class="hero-photo abs" role="img" aria-label="Photo of a machinist operating a CNC mill in the workshop"></div>
<div class="hero-caption abs">Specializes in Metal Works</div>
<div class="slider-dots abs"><span></span><span></span></div>

<aside class="hero-panel abs">
  <h2>We are a full-service<span>Corlinden Steel Forge</span></h2>
  <h3>Specializing in:</h3>
  <ul class="svc-list">
    <li>Machining</li><li>Welding</li><li>Powder Coating</li><li>Plasma Cutting</li><li>Forming</li><li>Prototyping</li>
  </ul>
  <div class="panel-btn">View our all services</div>
</aside>
<div class="contact-strip abs">
  Please call or email us with any questions.
  <div class="phone">555-014-2279</div>
  <div class="mail">CorlindenSteelForge@mailbox.example</div>
</div>

<article class="feature abs" style="left:150px">
  <div class="feature-photo" role="img" aria-label="Photo of precision cutting tools"></div>
  <div class="feature-title">About <em>Corlinden</em></div>
  <p class="feature-body">We cut, bend and weld steel to order with care, speed and fair prices for every shop and crew that trusts our floor each day.</p>
  <div class="read-more">Read more</div>
</article>
<article class="feature abs" style="left:455px">
  <div class="feature-photo" role="img" aria-label="Photo of a plasma cutter sending sparks over a steel sheet" style="background:linear-gradient(135deg,#c98a4a,#3a2a22)"></div>
  <div class="feature-title">Featured <em>Services</em></div>
  <p class="feature-body">From one part to long runs we handle milling, coating and forming in house so your order ships on time and to spec every time.</p>
  <div class="read-more">Read more</div>
</article>
<article class="feature abs" style="left:762px">
  <div class="feature-photo" role="img" aria-label="Photo of a lathe turning a metal part"></div>
  <div class="feature-title">Featured <em>Machines</em></div>
  <p class="feature-body">Our floor runs modern CNC mills, lathes and press brakes kept tuned by skilled hands for tight tolerance work on all metals.</p>
  <div class="read-more">Read more</div>
</article>

<footer class="site-footer abs"></footer>
<div class="foot-col abs" style="left:150px"><h4>Address:</h4>418 N Ridge Rd,<br>Harlow, TX 70012</div>
<div class="foot-col abs" style="left:380px"><h4>Call Us:</h4>Phone: 555-014-2279</div>
<div class="foot-col abs" style="left:635px"><h4>Email Us:</h4><a>CorlindenSteelForge@mailbox.example</a></div>
<div class="foot-col abs" style="left:885px"><h4>Office Hours:</h4>Monday - Friday 7:00AM to 5:30PM</div>
<div class="foot-bar abs">
  <span>Copyright © 2011 corlindensteelforge.example | Terms Of Use</span>
  <nav><a>Home</a><a>About Us</a><a>Our services</a><a>Our machines</a><a>Quote request</a><a>Contact Us</a></nav>
</div>
</body>
</html>
```